A restaurant needs a new design for menu and presentation flyers.

The name of the restaurant located in Germany is ,, GASTSTÄTTE ZUM TALHAHN" . It means RESTAURANT THE DALE ROOSTER. I attached two photos for reference to see the actual fonts.
I would like to have something close to the fonts we have now. I would like to add a crown representation.Any idea is welcomed.

Target Market(s)

GERMANY

Contact Information for Business Card

Must have ZUM TALHAHN logo.

Requirements
Nice to have
• A crown representation or other symbol who can be representative for our business.
An font close to actual fonts.

```html
<!DOCTYPE html>
<html lang="de">
<head>
<meta charset="utf-8">
<title>Zum Talhahn – Menu</title>
<link href="https://fonts.googleapis.com/css2?family=Pinyon+Script&family=Barlow+Condensed:wght@600&family=Pathway+Gothic+One&family=Heebo:wght@400;500;700&display=swap" rel="stylesheet">
<style>
  :root{
    --gold:#d5b56f;
    --gold-deep:#c9a45a;
    --panel:#1d1d1d;
    --paper:#ffffff;
    --ink:#1f1f1f;
    --muted:#707070;
  }
  *{margin:0;padding:0;box-sizing:border-box}
  html,body{width:1200px;height:856px;overflow:hidden;background:var(--paper)}
  .menu-sheet{position:relative;width:1200px;height:856px;background:var(--paper);font-family:"Heebo",sans-serif}

  /* left brand panel */
  .brand-panel{position:absolute;left:0;top:0;width:403px;height:856px;
    background:radial-gradient(ellipse at 50% 40%,#2a2a2a 0%,var(--panel) 70%,#161616 100%)}
  .brand-name{position:absolute;left:0;width:403px;top:268px;text-align:center;
    font-family:"Pinyon Script",cursive;font-size:66px;line-height:1;color:var(--gold)}
  .brand-rule{position:absolute;top:652px;left:128px;width:158px;height:10px}
  .contact-list{position:absolute;top:692px;left:0;width:403px;list-style:none;
    font-family:"Pathway Gothic One",sans-serif;font-size:17px;color:var(--gold);text-align:center}
  .contact-list li{height:29px;display:flex;align-items:center;justify-content:center;gap:8px}
  .contact-list svg{width:13px;height:13px;flex:none}

  /* menu side */
  .menu-title{position:absolute;top:46px;left:600px;width:386px;text-align:center;
    font-family:"Pinyon Script",cursive;font-size:52px;color:var(--gold);line-height:1.2}
  .menu-title::before,.menu-title::after{content:"";display:inline-block;width:5px;height:5px;
    background:var(--gold);transform:rotate(45deg);vertical-align:middle;margin:0 26px 14px}

  .section-tag{position:absolute;height:32px;background:var(--gold);color:#fff;
    font-family:"Barlow Condensed",sans-serif;font-weight:600;font-size:19px;letter-spacing:.2px;
    display:flex;align-items:center;padding-left:11px}
  .tag-main{left:454px;top:141px;width:121px;clip-path:polygon(0 0,100% 0,96% 100%,0 100%)}
  .tag-side{left:851px;top:141px;width:121px;clip-path:polygon(0 0,100% 0,96% 100%,0 100%)}
  .tag-drinks{left:726px;top:500px;width:137px;justify-content:center;padding:0;
    clip-path:polygon(4% 0,100% 0,96% 100%,0 100%)}

  .column-rule{position:absolute;left:794px;width:1px;background:var(--gold)}

  .dish{position:absolute;width:300px}
  .dish-name{font-size:17px;font-weight:400;color:var(--ink);letter-spacing:.3px;height:26px;
    display:flex;align-items:flex-end}
  .dish-name .initial{font-family:"Pinyon Script",cursive;font-size:30px;line-height:.9;margin-right:1px}
  .dish-desc{margin-top:5px;font-size:12px;line-height:15.5px;color:var(--muted);width:247px}
  .dish-desc .leader{letter-spacing:-1px;font-size:8px}
  .dish-price{position:absolute;left:260px;top:28px;color:var(--gold);font-weight:700;white-space:nowrap}
  .dish-price .currency{font-size:15px;vertical-align:top;position:relative;top:2px}
  .dish-price .amount{font-size:29px;font-weight:500}

  .photo-strip{position:absolute;top:653px;left:422px;display:flex;gap:8px}
  .photo{width:180px;height:169px}
  .photo-1{background:linear-gradient(150deg,#6b4a2c,#9b5a28 45%,#c9b48a)}
  .photo-2{background:linear-gradient(160deg,#3b2a1e,#a65a2e 50%,#5a3a22)}
  .photo-3{background:linear-gradient(150deg,#6d4a30,#d8c89a 50%,#8a5f3c)}
  .photo-4{background:linear-gradient(140deg,#7a4a24,#d7b47a 45%,#b98a52)}
</style>
</head>
<body>
<main class="menu-sheet">
  <aside class="brand-panel">
    <div class="brand-name">Zum Talhahn</div>
    <svg class="brand-rule" viewBox="0 0 158 10" aria-hidden="true">
      <line x1="0" y1="5" x2="70" y2="5" stroke="#d5b56f" stroke-width="1"/>
      <rect x="76" y="2" width="5" height="5" transform="rotate(45 78.5 4.5)" fill="none" stroke="#d5b56f"/>
      <line x1="88" y1="5" x2="158" y2="5" stroke="#d5b56f" stroke-width="1"/>
    </svg>
    <ul class="contact-list">
      <li><svg viewBox="0 0 12 16" aria-hidden="true"><path d="M6 0a6 6 0 0 0-6 6c0 4.5 6 10 6 10s6-5.5 6-10a6 6 0 0 0-6-6zm0 8.5A2.5 2.5 0 1 1 6 3.5a2.5 2.5 0 0 1 0 5z" fill="#fff"/></svg>Lindenweg 7, 36201 Talbach (Aue)</li>
      <li><svg viewBox="0 0 16 16" aria-hidden="true"><circle cx="8" cy="8" r="8" fill="#fff"/><path d="M5 3.5l1.6 2.3-.9 1.1c.5 1.2 1.5 2.2 2.6 2.7l1.1-.9 2.3 1.5-.6 1.6c-3.4.3-7.1-3.4-6.8-6.8z" fill="#1d1d1d"/></svg>Frau Lena Berger 170 55512340</li>
      <li><svg viewBox="0 0 16 16" aria-hidden="true"><circle cx="8" cy="8" r="8" fill="#fff"/></svg>/ZumTalhahnTalbach</li>
    </ul>
  </aside>

  <h1 class="menu-title">Menu</h1>

  <div class="section-tag tag-main">MAIN DISHES</div>
  <div class="section-tag tag-side">SIDE DISHES</div>
  <div class="column-rule" style="top:194px;height:260px"></div>

  <article class="dish" style="left:456px;top:190px">
    <h2 class="dish-name"><span class="initial">S</span>INT OCCAECAT</h2>
    <p class="dish-desc">Sed ut perspiciatis unde omnis iste natus error sit voluptatem accusantium<span class="leader">..............................</span></p>
    <div class="dish-price"><span class="currency">€</span><span class="amount">5</span></div>
  </article>
  <article class="dish" style="left:456px;top:290px">
    <h2 class="dish-name"><span class="initial">Q</span>UIS NOSTRUD</h2>
    <p class="dish-desc">Sed ut perspiciatis unde omnis iste natus error sit voluptatem accusantium<span class="leader">..............................</span></p>
    <div class="dish-price"><span class="currency">€</span><span class="amount">7</span></div>
  </article>
  <article class="dish" style="left:456px;top:390px">
    <h2 class="dish-name"><span class="initial">E</span>USMOD TEMPOR</h2>
    <p class="dish-desc">Sed ut perspiciatis unde omnis iste natus error sit voluptatem accusantium<span class="leader">..............................</span></p>
    <div class="dish-price"><span class="currency">€</span><span class="amount">8</span></div>
  </article>

  <article class="dish" style="left:853px;top:190px">
    <h2 class="dish-name"><span class="initial">S</span>INT OCCAECAT</h2>
    <p class="dish-desc">Sed ut perspiciatis unde omnis iste natus error sit voluptatem accusantium<span class="leader">..............................</span></p>
    <div class="dish-price"><span class="currency">€</span><span class="amount">5</span></div>
  </article>
  <article class="dish" style="left:853px;top:290px">
    <h2 class="dish-name"><span class="initial">Q</span>UIS NOSTRUD</h2>
    <p class="dish-desc">Sed ut perspiciatis unde omnis iste natus error sit voluptatem accusantium<span class="leader">..............................</span></p>
    <div class="dish-price"><span class="currency">€</span><span class="amount">7</span></div>
  </article>
  <article class="dish" style="left:853px;top:390px">
    <h2 class="dish-name"><span class="initial">E</span>USMOD TEMPOR</h2>
    <p class="dish-desc">Sed ut perspiciatis unde omnis iste natus error sit voluptatem accusantium<span class="leader">..............................</span></p>
    <div class="dish-price"><span class="currency">€</span><span class="amount">8</span></div>
  </article>

  <div class="section-tag tag-drinks">DRINKS</div>
  <div class="column-rule" style="top:553px;height:61px"></div>

  <article class="dish" style="left:456px;top:549px">
    <h2 class="dish-name"><span class="initial">S</span>INT OCCAECAT</h2>
    <p class="dish-desc">Sed ut perspiciatis unde omnis iste natus error sit voluptatem accusantium<span class="leader">..............................</span></p>
    <div class="dish-price"><span class="currency">€</span><span class="amount">5</span></div>
  </article>
  <article class="dish" style="left:853px;top:549px">
    <h2 class="dish-name"><span class="initial">S</span>INT OCCAECAT</h2>
    <p class="dish-desc">Sed ut perspiciatis unde omnis iste natus error sit voluptatem accusantium<span class="leader">..............................</span></p>
    <div class="dish-price"><span class="currency">€</span><span class="amount">5</span></div>
  </article>

  <div class="photo-strip">
    <div class="photo photo-1" role="img" aria-label="Roast pork knuckle with sauerkraut and a glass of beer"></div>
    <div class="photo photo-2" role="img" aria-label="Grilled sausages in a cast-iron pan"></div>
    <div class="photo photo-3" role="img" aria-label="Potato dumplings with bacon and herbs"></div>
    <div class="photo photo-4" role="img" aria-label="Sausage in a bun with sauerkraut and mustard"></div>
  </div>
</main>
</body>
</html>
```